Country Music Cruise Design

Current site
www.rhinestonewaves.com/index.php

We want a site that is Vibrant and Colorful with cartoon style graphics. This will be a bootstrap site and shall use that idea when designing.

We want a mixture of the two sites which we really like
http://www.banjoharborvoyage.com/
and
https://drifterjam.net

Our logo is attached
Need a really nice one page design homepage with information and one page for the booking (www.rhinestonewaves.com/book)

Target Market(s)

country music fans on a cruise ship, 20-50 year old

Coding

Coded - Design and coding required

Number of Pages Required

4 page

Font styles to use
Sans Serif

Requirements
Must have
• Vibrant style colors and backgrounds like examples above.
Should not have
• Dark color

```html
<!DOCTYPE html>
<html lang="en">
<head>
<meta charset="utf-8">
<title>Rhinestone Waves Cruise — Highlights</title>
<link rel="stylesheet" href="https://fonts.googleapis.com/css2?family=Bitter:wght@400&family=Work+Sans:wght@400;500;600&display=swap">
<style>
  :root {
    --white: #ffffff;
    --page-grey: #f1f1f1;
    --accent: #f26a2e;
    --icon-orange: #f7901e;
    --heading: #111111;
    --body-text: #7a7a7a;
    --nav-text: #333333;
    --ocean-top: #3f6687;
    --ocean-bottom: #5a82a5;
    --top-btn: #efefef;
  }
  * { box-sizing: border-box; margin: 0; padding: 0; }
  html, body { width: 1200px; height: 666px; overflow: hidden; background: var(--white); }
  body { position: relative; font-family: "Work Sans", Arial, sans-serif; }

  .site-nav {
    position: absolute; top: 0; left: 0; width: 1200px; height: 57px;
    background: var(--white); z-index: 3;
    box-shadow: 0 1px 4px rgba(0,0,0,0.08);
  }
  .site-nav__menu {
    position: absolute; left: 52px; top: 17px; display: flex; gap: 23px; list-style: none;
  }
  .site-nav__menu a {
    font-family: "Bitter", Georgia, serif; font-size: 14px; color: var(--nav-text);
    text-decoration: none; letter-spacing: 0.2px;
  }
  .site-nav__cart { position: absolute; left: 1108px; top: 17px; display: flex; align-items: center; gap: 4px; }

  .ocean-band {
    position: absolute; left: 12px; top: 57px; width: 1176px; height: 65px;
    background: linear-gradient(180deg, var(--ocean-top), var(--ocean-bottom));
  }
  .highlights {
    position: absolute; left: 12px; top: 122px; width: 1176px; height: 458px;
    background: var(--page-grey);
  }

  .feature-card {
    position: absolute; top: 76px; width: 343px;
    background: var(--white); z-index: 2;
    box-shadow: 0 8px 14px rgba(0,0,0,0.12);
    display: flex; flex-direction: column; align-items: center;
    padding-top: 24px; text-align: center;
  }
  .feature-card--included { left: 57px; height: 321px; }
  .feature-card--activities { left: 428px; height: 347px; }
  .feature-card--itinerary { left: 800px; height: 398px; }

  .feature-card__icon { width: 58px; height: 58px; }
  .feature-card__icon--crowd {
    background: linear-gradient(180deg, var(--icon-orange), #f47b1f);
    border-radius: 4px;
  }
  .feature-card__title {
    margin-top: 29px; font-size: 14px; font-weight: 500; letter-spacing: 2.6px;
    color: var(--heading);
  }
  .feature-card__rule { width: 38px; height: 2px; background: var(--accent); margin-top: 9px; }
  .feature-card__text {
    margin-top: 13px; font-size: 14.6px; line-height: 25.8px; color: var(--body-text);
    padding: 0 22px;
  }
  .feature-card__button {
    margin-top: 16px; width: 98px; height: 40px; border: 1px solid var(--accent);
    border-radius: 20px; color: var(--accent); font-size: 14.5px;
    display: flex; align-items: center; justify-content: center; gap: 6px;
    text-decoration: none;
  }

  .back-to-top {
    position: absolute; left: 1126px; top: 574px; width: 48px; height: 48px;
    border-radius: 50%; background: var(--top-btn);
    display: flex; align-items: center; justify-content: center;
  }
</style>
</head>
<body>
  <header class="site-nav">
    <ul class="site-nav__menu">
      <li><a href="#">PRICES</a></li>
      <li><a href="#">WHAT'S INCLUDED?</a></li>
      <li><a href="#">FAQ'S</a></li>
      <li><a href="#">SHOP</a></li>
      <li><a href="#">BOOK NOW</a></li>
    </ul>
    <div class="site-nav__cart" aria-label="Cart">
      <svg width="17" height="16" viewBox="0 0 17 16" fill="none" stroke="#222" stroke-width="1.8">
        <path d="M1 2h2.5l2 8h8l2-6H5"/>
        <circle cx="7" cy="13.5" r="1.2" fill="#222"/><circle cx="12.5" cy="13.5" r="1.2" fill="#222"/>
      </svg>
      <svg width="7" height="5" viewBox="0 0 7 5"><path d="M0 0h7L3.5 4z" fill="#aaa"/></svg>
    </div>
  </header>

  <div class="ocean-band" role="img" aria-label="Photo of the open blue ocean"></div>
  <section class="highlights"></section>

  <article class="feature-card feature-card--included">
    <svg class="feature-card__icon" viewBox="0 0 58 58" fill="none" stroke="var(--icon-orange)" stroke-width="2.2" stroke-linejoin="round">
      <path d="M27 3h4v5"/>
      <rect x="19" y="8" width="20" height="7"/>
      <rect x="13" y="15" width="32" height="10"/>
      <path d="M17 19h4M25 19h4M33 19h4"/>
      <path d="M6 25h46l-6 20H12z"/>
      <path d="M29 25v20"/>
      <path d="M2 52c4-3 7-3 10 0s7 3 10 0 7-3 10 0 7 3 10 0 7-3 10 0"/>
    </svg>
    <h2 class="feature-card__title">WHAT'S INCLUDED?</h2>
    <span class="feature-card__rule"></span>
    <p class="feature-card__text">All RWC events, Food, Comedy Club,<br>Kids Clubs, Game Shows, Night Clubs,<br>GYM, Bars and Water Park</p>
    <a class="feature-card__button" href="#">More
      <svg width="13" height="12" viewBox="0 0 13 12" fill="none" stroke="currentColor" stroke-width="1.4"><path d="M1 6h11M7 1l5 5-5 5"/></svg>
    </a>
  </article>

  <article class="feature-card feature-card--activities">
    <div class="feature-card__icon feature-card__icon--crowd" role="img" aria-label="Icon of a cheering crowd with a dancer in front"></div>
    <h2 class="feature-card__title">RWC ACTIVITIES</h2>
    <span class="feature-card__rule"></span>
    <p class="feature-card__text">We will bring on bands, Southern<br>California's favorite DJ's, Line Dance<br>Lessons, Two Stepping, Contest,<br>Offshore Parties and much much more</p>
    <a class="feature-card__button" href="#">More
      <svg width="13" height="12" viewBox="0 0 13 12" fill="none" stroke="currentColor" stroke-width="1.4"><path d="M1 6h11M7 1l5 5-5 5"/></svg>
    </a>
  </article>

  <article class="feature-card feature-card--itinerary">
    <svg class="feature-card__icon" viewBox="0 0 58 58" fill="none" stroke="var(--icon-orange)" stroke-width="2">
      <rect x="2" y="6" width="54" height="50"/>
      <path d="M2 16h54"/>
      <circle cx="20" cy="5" r="3"/><circle cx="26" cy="5" r="3"/><circle cx="32" cy="5" r="3"/><circle cx="38" cy="5" r="3"/>
      <g fill="var(--icon-orange)" stroke="none">
        <circle cx="20" cy="24" r="1"/><circle cx="27" cy="24" r="1"/><circle cx="34" cy="24" r="1"/><circle cx="41" cy="24" r="1"/><circle cx="48" cy="24" r="1"/>
        <circle cx="9" cy="31" r="1"/><circle cx="16" cy="31" r="1"/><circle cx="23" cy="31" r="1"/><circle cx="30" cy="31" r="1"/><circle cx="37" cy="31" r="1"/><circle cx="44" cy="31" r="1"/>
        <circle cx="9" cy="38" r="1"/><circle cx="16" cy="38" r="1"/><circle cx="23" cy="38" r="1"/><circle cx="30" cy="38" r="1"/><circle cx="37" cy="38" r="1"/><circle cx="44" cy="38" r="1"/>
        <circle cx="9" cy="45" r="1"/><circle cx="16" cy="45" r="1"/><circle cx="23" cy="45" r="1"/><circle cx="30" cy="45" r="1"/>
      </g>
    </svg>
    <h2 class="feature-card__title">SHIP ITINERARY</h2>
    <span class="feature-card__rule"></span>
    <p class="feature-card__text">January 12th -15th<br>Friday - Leave Port 5:30 PM<br>Saturday - Ensenada Mexico | Formal<br>Dinner<br>Sunday - Day at Sea<br>Monday - 7am Return to port</p>
    <a class="feature-card__button" href="#">More
      <svg width="13" height="12" viewBox="0 0 13 12" fill="none" stroke="currentColor" stroke-width="1.4"><path d="M1 6h11M7 1l5 5-5 5"/></svg>
    </a>
  </article>

  <a class="back-to-top" href="#" aria-label="Back to top">
    <svg width="16" height="10" viewBox="0 0 16 10" fill="none" stroke="#222" stroke-width="2"><path d="M1 9l7-7 7 7"/></svg>
  </a>
</body>
</html>
```